Instagram adverts for international jewellery making school

We need 10 single image Instagram adverts to promote our jewellery school in Kuala Lumpur Malaysia to an international market. The images should all have a different feel and it is up to the designer to also come up with wording to include on the images - you can refer to our website for details on the classes https://maradenholtcraft.com/starter-2. <br/><br/>The feeling and wording should be fun, vibrant and quirky - no need to be too serious here, and I generally prefer busier images - they won't be used for promotional posts so no need to worry about Instagram / FB ad restrictions<br/><br/>We have attached an example of one Instagram ad we created ourselves for reference.<br/><br/>We only need to see one advert before selecting you as a designer and we are looking to build an ongoing relationship for all future graphic design needs. <br/><br/>We will send a google drive of images to the chosen designer but for now, please just use the images from the website for the prototype.

Font styles to use
Serif
Sans Serif

Colors

Designer to choose colors to be used in the design.

Requirements
Must have
• Fun bold vibrant feel
Nice to have
• Multiple images included in each post

```html
<!DOCTYPE html>
<html lang="en">
<head>
<meta charset="utf-8">
<title>Mara Denholt Craft – Instagram adverts</title>
<link href="https://fonts.googleapis.com/css2?family=Questrial&display=swap" rel="stylesheet">
<style>
  :root {
    --canvas: #e9eaec;
    --pink: #f0848f;
    --white: #ffffff;
    --ink: #58595b;
    --ink-dark: #474749;
    --ink-soft: #77787b;
    --blush-1: #fbe4dd;
    --blush-2: #f4cfc6;
    --blush-3: #fdf5f2;
    --teal: #3f8f93;
  }
  * { margin: 0; padding: 0; box-sizing: border-box; }
  html, body { width: 1200px; height: 444px; overflow: hidden; }
  body {
    background: var(--canvas);
    font-family: "Questrial", "Century Gothic", sans-serif;
    color: var(--ink);
    position: relative;
  }
  .advert {
    position: absolute;
    top: 40px;
    width: 354px;
    height: 354px;
    overflow: hidden;
    background: linear-gradient(135deg, var(--blush-3) 0%, var(--blush-2) 30%, var(--blush-3) 55%, var(--blush-1) 75%, var(--blush-3) 100%);
    box-shadow: 6px 10px 14px rgba(0,0,0,0.22);
  }
  .advert--designer { left: 50px; }
  .advert--kickstarter { left: 423px; }
  .advert--classes { left: 797px; }
  .block { position: absolute; }
  .pink { background: var(--pink); }
  .white { background: var(--white); }
  .photo { position: absolute; }

  .photo--sketches {
    background:
      radial-gradient(circle at 22% 28%, #c2345a 0 9%, transparent 22%),
      radial-gradient(circle at 62% 40%, #3fb3a8 0 10%, transparent 26%),
      radial-gradient(circle at 84% 18%, #a0233f 0 7%, transparent 20%),
      radial-gradient(circle at 40% 70%, #e15c86 0 8%, transparent 24%),
      radial-gradient(circle at 80% 74%, #2f8f7f 0 7%, transparent 22%),
      linear-gradient(135deg, #eeebe3 0%, #e4dfd6 100%);
  }
  .photo--rings-hand {
    background:
      radial-gradient(ellipse at 48% 30%, #e0345e 0 8%, transparent 20%),
      radial-gradient(ellipse at 45% 50%, #b43a5c 0 8%, transparent 20%),
      radial-gradient(ellipse at 62% 60%, #6fb1e2 0 8%, transparent 20%),
      radial-gradient(ellipse at 48% 70%, #f4f1ee 0 7%, transparent 18%),
      radial-gradient(ellipse at 52% 84%, #7c9890 0 7%, transparent 18%),
      linear-gradient(170deg, #d8c3b8 0%, #d39c86 45%, #b27d6c 70%, #2e2626 100%);
  }
  .photo--stacking-rings {
    background:
      radial-gradient(ellipse at 15% 35%, #8a3fb0 0 6%, transparent 14%),
      linear-gradient(90deg, transparent 0 4%, #b8913e 4% 8%, transparent 8% 14%, #9e9fa3 14% 17%, transparent 17% 24%, #c9a35a 24% 27%, transparent 27% 34%, #d8d8d8 34% 37%, transparent 37% 44%, #d29a6b 44% 47%, transparent 47% 54%, #bfbfc2 54% 57%, transparent 57% 64%, #d08a5e 64% 67%, transparent 67% 74%, #c9a35a 74% 77%, transparent 77% 84%, #b57a4c 84% 87%, transparent 87% 94%, #8d8d91 94% 97%, transparent 97%),
      linear-gradient(180deg, #f7f7f7 0%, #ececec 100%);
  }
  .photo--cuff-rings {
    background:
      linear-gradient(90deg, #f4f4f4 0 5%, #d69a78 5% 20%, #f4f4f4 20% 25%, #7b4c33 25% 40%, #f4f4f4 40% 45%, #c9a23a 45% 58%, #f4f4f4 58% 65%, #c57e5c 65% 78%, #f4f4f4 78% 83%, #b9bbbe 83% 95%, #f4f4f4 95%);
  }

  .brand {
    position: absolute;
    background: var(--white);
    display: flex;
    flex-direction: column;
    align-items: center;
    justify-content: center;
    color: var(--ink);
    text-align: center;
  }
  .brand__dot { border: 1.5px solid var(--teal); border-radius: 50%; }
  .brand__name { letter-spacing: 0.04em; line-height: 1; white-space: nowrap; }
  .brand__sub { letter-spacing: 0.12em; line-height: 1; }

  .url { position: absolute; white-space: nowrap; line-height: 1; font-size: 15.5px; }
  .url__lead { color: var(--ink-soft); }
  .url--light .url__lead { color: var(--white); opacity: 0.85; }

  .designer__headline {
    position: absolute; left: 0; top: 272px; width: 354px; height: 48px;
    background: var(--pink); color: var(--white);
    font-size: 23px; line-height: 20px; text-align: center; padding-top: 4px;
  }
  .kickstarter__title {
    position: absolute; left: 22px; top: 306px;
    transform: rotate(-90deg); transform-origin: 0 0;
    font-size: 29px; line-height: 26px; color: var(--ink-dark);
    white-space: nowrap;
  }
  .classes__title {
    position: absolute; left: 0; top: 20px; width: 354px;
    text-align: center; font-size: 25px; line-height: 20px; color: var(--ink-dark);
  }
</style>
</head>
<body>

  <section class="advert advert--designer">
    <div class="block pink" style="left:0;top:68px;width:354px;height:101px;"></div>
    <div class="block white" style="left:30px;top:0;width:293px;height:226px;"></div>
    <div class="photo photo--sketches" role="img" aria-label="Sketches of gem jewellery designs with loose pink and green tourmaline stones"
         style="left:44px;top:0;width:266px;height:212px;"></div>
    <div class="brand" style="left:112px;top:159px;width:130px;height:102px;">
      <div class="brand__dot" style="width:46px;height:46px;margin-bottom:8px;"></div>
      <div class="brand__name" style="font-size:15px;">MARA DENHOLT</div>
      <div class="brand__sub" style="font-size:8.5px;margin-top:5px;">craft</div>
    </div>
    <h2 class="designer__headline">So you want to be<br>a jewellery designer ?</h2>
    <div class="block white" style="left:0;top:320px;width:354px;height:34px;"></div>
    <p class="url" style="left:61px;top:330px;color:var(--ink);">
      <span class="url__lead">visit us</span> <span class="url__site">maradenholtcraft.com</span>
    </p>
  </section>

  <section class="advert advert--kickstarter">
    <div class="block pink" style="left:198px;top:0;width:156px;height:354px;"></div>
    <div class="block white" style="left:96px;top:59px;width:228px;height:248px;"></div>
    <div class="photo photo--rings-hand" role="img" aria-label="Hand held towards the camera wearing five rose gold rings with pink, blue, moonstone and labradorite stones"
         style="left:108px;top:70px;width:205px;height:225px;"></div>
    <div class="brand" style="left:242px;top:16px;width:68px;height:69px;">
      <div class="brand__dot" style="width:26px;height:26px;margin-bottom:6px;"></div>
      <div class="brand__name" style="font-size:7.5px;">MARA DENHOLT</div>
      <div class="brand__sub" style="font-size:5px;margin-top:3px;">craft</div>
    </div>
    <h2 class="kickstarter__title">Jewellery Making<br>Kickstarter</h2>
    <div class="block white" style="left:56px;top:314px;width:243px;height:27px;"></div>
    <p class="url" style="left:66px;top:320px;color:var(--ink);">
      <span class="url__lead">visit us</span> <span class="url__site">maradenholtcraft.com</span>
    </p>
  </section>

  <section class="advert advert--classes">
    <h2 class="classes__title">Online classes are coming<br>in March 2020</h2>
    <div class="block pink" style="left:0;top:149px;width:354px;height:89px;"></div>
    <div class="block white" style="left:21px;top:71px;width:312px;height:111px;"></div>
    <div class="photo photo--stacking-rings" role="img" aria-label="Row of stacking rings in gold, silver and rose gold with clear and amethyst stones"
         style="left:32px;top:81px;width:290px;height:90px;"></div>
    <div class="block white" style="left:21px;top:205px;width:312px;height:110px;"></div>
    <div class="photo photo--cuff-rings" role="img" aria-label="Five wide cuff rings in copper, rose gold, brass and silver with pierced textures"
         style="left:32px;top:215px;width:290px;height:90px;"></div>
    <div class="brand" style="left:140px;top:165px;width:75px;height:49px;">
      <div class="brand__dot" style="width:26px;height:26px;margin-bottom:5px;"></div>
      <div class="brand__name" style="font-size:8px;">MARA DENHOLT</div>
      <div class="brand__sub" style="font-size:5px;margin-top:3px;">craft</div>
    </div>
    <div class="block pink" style="left:0;top:320px;width:354px;height:20px;"></div>
    <p class="url url--light" style="left:66px;top:323px;color:var(--white);">
      <span class="url__lead">visit us</span> <span class="url__site">maradenholtcraft.com</span>
    </p>
  </section>

</body>
</html>
```